Business Card Design of an established Waste Management, Plastic Recycling and Renewable Energy Comp

We are looking for business card design for plastic card with holograms (Very similar to credit card). I will provide our logo (Fenwicks). So the name on the business card will be our logo )Fenwicks) + Environmental next to it, so it will read Fenwicks Environmental. The font for Environmental does not to be the same as the font of the logo. The holograms will be used to display ISO14001 Certified (In normal credit card, normally on the holograms, they show zenra or corvo). I will post the design requirements from the card printing company very shortly to make sure they can use the design for the plastic card.

Target Market(s)

Companies, Government Organizations, Corporations.

Industry/Entity Type

Business

Contact Information for Business Card

Motto (Under the logo): Care In Every Load
Name: Bertolus Kemprano; Position: Business Manager; Address: Kestrel Vale Landfill & Recycling Facility, Wexcombe Rd, Marrowbank, WA 6931; Ph: +61 8 5021 3748; Mob: +61 400 917 352; E: Bertie@fenwicksenvironmental-mail.example

Requirements
Must have
• Business Names: Fenwicks Logo + Environmental word after the logo.
• Motto (Under the logo): Care In Every Load
• All the Business Card Details above.
• Hologram Logo on the lower right corner which says: ISO 14001 Certified.
• Please remember the design will be printed on plastic card Not paper. The plastic crad is the same as credit card. Hope this helps. Thank You

```html
<!DOCTYPE html>
<html lang="en">
<head>
<meta charset="utf-8">
<title>Fenwicks Environmental – Business Card</title>
<link rel="stylesheet" href="https://fonts.googleapis.com/css2?family=Montserrat:wght@400;500;600;700&display=swap">
<style>
  :root {
    --stage: #2c2a2b;
    --card: #dfe1e4;
    --ink: #3a3d42;
    --ink-soft: #4a4d52;
    --blue: #1f72bb;
    --blue-deep: #164a8c;
    --badge-line: #8a8d92;
  }
  * { margin: 0; padding: 0; box-sizing: border-box; }
  html, body { width: 846px; height: 1200px; overflow: hidden; }
  body {
    background: var(--stage);
    font-family: "Montserrat", sans-serif;
    color: var(--ink);
    position: relative;
  }
  .card {
    position: absolute;
    left: 122px;
    width: 602px;
    height: 334px;
    background: var(--card);
    border-radius: 22px;
  }
  .card--front { top: 176px; }
  .card--back { top: 766px; }

  .brand { position: absolute; left: 34px; top: 40px; }
  .brand__dot {
    position: absolute; left: 0; top: 4px;
    width: 56px; height: 56px; border-radius: 50%;
    background: linear-gradient(135deg, var(--blue), var(--blue-deep));
  }
  .brand__name {
    position: absolute; left: 76px; top: -4px;
    font-size: 44px; font-weight: 600; color: var(--ink);
    white-space: nowrap; line-height: 1;
  }
  .brand__sub {
    position: absolute; left: 78px; top: 48px;
    font-size: 19px; font-weight: 500; letter-spacing: 4px;
    white-space: nowrap; line-height: 1;
  }
  .brand__motto {
    position: absolute; left: 78px; top: 72px;
    font-size: 10.5px; letter-spacing: 4px; white-space: nowrap; line-height: 1;
  }

  .person { position: absolute; left: 35px; top: 158px; line-height: 1; }
  .person__name { font-size: 16.5px; font-weight: 600; color: var(--blue); }
  .person__role { margin-top: 5px; font-size: 13px; color: var(--ink-soft); }

  .contact { position: absolute; left: 35px; top: 206px; list-style: none; font-size: 13px; }
  .contact li { display: flex; align-items: center; height: 18.5px; white-space: nowrap; }
  .contact .contact__email { font-size: 11.5px; }
  .contact svg { width: 12px; height: 12px; margin-right: 6px; fill: var(--blue); flex: none; }

  .address { position: absolute; left: 35px; top: 268px; font-size: 13px; line-height: 17.5px; font-style: normal; white-space: nowrap; }

  .cert-badge {
    position: absolute; left: 198px; top: 190px; width: 61px; height: 44px;
    border: 1.2px solid var(--badge-line); border-radius: 5px;
  }
  .cert-badge::after {
    content: ""; position: absolute; left: 17px; top: 9px;
    width: 26px; height: 26px; border-radius: 50%; border: 1px solid var(--badge-line);
  }

  .emblem {
    position: absolute; border-radius: 50%;
    background: linear-gradient(140deg, var(--blue) 20%, var(--blue-deep));
    display: flex; align-items: center; justify-content: center;
    color: #fff; font-weight: 600; font-size: 28px;
  }
  .card--front .emblem { left: 362px; top: 88px; width: 206px; height: 206px; }
  .card--back .emblem { left: 46px; top: 82px; width: 216px; height: 216px; }

  .back-motto {
    position: absolute; left: 310px; top: 178px;
    font-size: 14px; letter-spacing: 6px; white-space: nowrap;
  }
</style>
</head>
<body>
  <section class="card card--front">
    <div class="brand">
      <span class="brand__dot"></span>
      <span class="brand__name">Fenwicks</span>
      <span class="brand__sub">Environmental</span>
      <span class="brand__motto">Care In Every Load</span>
    </div>

    <div class="person">
      <p class="person__name">Bertolus Kemprano</p>
      <p class="person__role">Business Manager</p>
    </div>

    <ul class="contact">
      <li><svg viewBox="0 0 12 12"><path d="M1 4c0-2 2-3 5-3s5 1 5 3v1H8V4H4v1H1zM2 6h8l1 5H1z"/></svg>+61 8 5021 3748</li>
      <li><svg viewBox="0 0 12 12"><rect x="3" y="1" width="6" height="3"/><rect x="1" y="4" width="10" height="5" rx="1"/><rect x="3" y="8" width="6" height="3"/></svg>+61 400 917 352</li>
      <li class="contact__email"><svg viewBox="0 0 12 12"><path d="M1 3h10v6H1zM1 3l5 4 5-4" stroke="#dfe1e4" stroke-width="0.8"/></svg>bertie@fenwicksenvironmental-mail.example</li>
    </ul>

    <address class="address">Kestrel Vale Landfill &amp; Recycling Facility,<br>Wexcombe Rd, Marrowbank, WA 6931</address>

    <div class="cert-badge" role="img" aria-label="Certification hologram area"></div>

    <div class="emblem">Fenwicks</div>
  </section>

  <section class="card card--back">
    <div class="emblem">Fenwicks</div>
    <p class="back-motto">Care In Every Load</p>
  </section>
</body>
</html>
```